Maple Brook Concrete business card design

We need a business card developed for a local ready mix concrete company. We want a 2 sided design

The front just needs the basic contact info:

Raymond Vasquelli
P.555-014-2261
F. 555-014-2287
www.MapleBrookConcrete.Com
Raymond@MapleBrookConcrete.com
P.O Box 614
Succasunna, NJ, 07192

Service All of North And Central New Jersey With Ready Mix Concrete

The back will have a simple bullet point list:
• Metered Delivery - Use only what you pay for
• No Waste
• Multiple slumps on the fly
• No minimum delivery
• 24-7 service, all year
• No Hot Loads
• Fastest Service in the industry
Updates

I like the submissions using the existing colors. I think blue might also be a color to use as well. For the next trucks we order we will probably paint them blue. Colbalt blue

I must have made a typo: It should read, Serving all of North and Central New Jersey. It should also say: Pay for only what you use.

Target Market(s)

We will be targeting the construction industry

Industry/Entity Type

Concrete

Font styles to use
Serif
Sans Serif

Colors
ec2027

Requirements
Must have
• It needs to have a clean uncluttered look. The back is dedicated to telling customer what we do. Our advantage is we use a truck that delivers concrete with several advantages over barrel trucks, hence, why the back bullet points are important
Nice to have
• Our logo. I think since our logo is green, the front might look good with some red, like a red background (also the color of our truck)
Should not have
• clip art.

```html
<!DOCTYPE html>
<html lang="en">
<head>
<meta charset="UTF-8">
<title>Maple Brook Concrete – Business Card Back</title>
<link rel="stylesheet" href="https://fonts.googleapis.com/css2?family=Fira+Sans:wght@300;600&display=swap">
<style>
  :root {
    --backdrop: #f1f1f1;
    --concrete: #c9c9c7;
    --concrete-dark: #b3b3b1;
    --panel-green: #a6cc3a;
    --panel-shadow: rgba(0, 0, 0, 0.28);
    --ink: #1c1c1c;
    --accent: #c4114c;
  }
  html, body {
    margin: 0;
    padding: 0;
    overflow: hidden;
  }
  .card {
    position: relative;
    width: 1200px;
    height: 686px;
    overflow: hidden;
    background: var(--backdrop);
    font-family: "Fira Sans", sans-serif;
  }
  .concrete-texture {
    position: absolute;
    left: 0;
    top: 0;
    width: 354px;
    height: 686px;
    background: radial-gradient(ellipse at 40% 40%, var(--concrete) 0%, var(--concrete-dark) 100%);
  }
  .benefits-panel {
    position: absolute;
    left: 352px;
    top: 80px;
    width: 848px;
    height: 523px;
    background: var(--panel-green);
    box-shadow: 0 6px 10px var(--panel-shadow);
  }
  .benefits-list {
    list-style: none;
    margin: 0;
    padding: 0;
    position: absolute;
    left: 86px;
    top: 42px;
  }
  .benefit {
    position: relative;
    padding-left: 22px;
    font-weight: 300;
    font-size: 37px;
    line-height: 51.5px;
    color: var(--ink);
    white-space: nowrap;
  }
  .benefit::before {
    content: "";
    position: absolute;
    left: 0;
    top: 27px;
    width: 5px;
    height: 5px;
    background: currentColor;
  }
  .benefit--highlight {
    color: var(--accent);
    font-weight: 600;
    letter-spacing: -0.3px;
  }
  .benefit--metered {
    margin-top: 5px;
  }
  .benefit-note {
    display: block;
    margin-top: 4px;
    padding-left: 169px;
    font-size: 31px;
    line-height: 44px;
    font-weight: 300;
    color: var(--ink);
  }
</style>
</head>
<body>
  <div class="card">
    <div class="concrete-texture" role="img" aria-label="Grey poured concrete surface texture"></div>
    <section class="benefits-panel">
      <ul class="benefits-list">
        <li class="benefit">No Waste</li>
        <li class="benefit">Multiple slumps on the fly</li>
        <li class="benefit">No minimum delivery</li>
        <li class="benefit">24-7 service, all year</li>
        <li class="benefit">No Hot Loads</li>
        <li class="benefit benefit--highlight">Fastest Service in the industry</li>
        <li class="benefit benefit--metered">Metered Delivery
          <span class="benefit-note">Use only what you pay for</span>
        </li>
      </ul>
    </section>
  </div>
</body>
</html>
```